Maple Cove Laser Dermal Studio needs an 8 page WP redesign

We need a colorful re-design for an 8 page Wordpress website. The current preliminary website is live. The home page URL is http://maplecovelaserdermalstudio.com The new logo is live on the website also. I would like a (re)design using the colors that are represented by the new logo file, and any additional complimentary colors. The information regarding the business can be found on the website already, so please review it for insight. The name of the business is "Maple Cove Laser Dermal Studio".

Target Market(s)

The targeted website viewer is an adult female between the ages of 30 and 75 who is interested in facial renewal, wart removal and scar removal. This website should inspire in the target viewer the benefits of laser facial renewal, wart removal and new scar removal. Potential website viewers are wanting and searching for improved skin health and appearance. The website must represent the essence of a professional spa business.

Industry/Entity Type

Business

Font styles to use
Sans Serif

Requirements
Must have
• - The phone number placed in a visible and high value widget area that allows mobile phone browser dialing.

```html
<!DOCTYPE html>
<html lang="en">
<head>
<meta charset="utf-8">
<title>Maple Cove Laser Dermal Studio</title>
<link href="https://fonts.googleapis.com/css2?family=Didact+Gothic&family=Open+Sans:wght@400;600&display=swap" rel="stylesheet">
<style>
:root{
  --pink:#c8317d;
  --pink-deep:#a8226c;
  --magenta:#d63e95;
  --purple:#7a2c8f;
  --violet:#8c3fb8;
  --dark:#2f2a30;
  --darker:#242026;
  --bar:#4a4249;
  --white:#ffffff;
  --text:#555;
  --light:#f3e6ef;
}
*{margin:0;padding:0;box-sizing:border-box}
html,body{width:779px;height:1200px;overflow:hidden;background:var(--white)}
body{position:relative;font-family:"Open Sans",sans-serif;color:var(--text)}
.head{font-family:"Didact Gothic",sans-serif}
.abs{position:absolute}

.site-header{position:absolute;left:0;top:0;width:779px;height:87px;
  background:linear-gradient(90deg,#d2458f,#e05aa3 40%,#c23a87 70%,#d04d98)}
.brand{position:absolute;left:52px;top:22px;width:180px;color:var(--white);
  font-family:"Didact Gothic",sans-serif;font-size:17px;line-height:20px}
.nav{position:absolute;left:243px;top:26px;display:flex;gap:0}
.nav a{color:var(--white);text-decoration:none;font-family:"Didact Gothic",sans-serif;
  font-size:12.5px;padding:0 11px;line-height:28px;border:1px solid transparent}
.nav a.active{border-color:rgba(255,255,255,.85);border-radius:2px;padding:0 11px;margin-right:1px}

.hero{position:absolute;left:0;top:87px;width:779px;height:236px;overflow:hidden}
.hero-left{position:absolute;left:0;top:0;width:505px;height:236px;background:linear-gradient(90deg,#d9d9d9,#f2f2f2 60%,#e6e6e6)}
.hero-right{position:absolute;left:505px;top:0;width:274px;height:236px;background:linear-gradient(90deg,#f4e1ea,#efc9a8 55%,#e8b898)}
.hero-photo{position:absolute;left:248px;top:25px;width:190px;height:190px;border-radius:50%;background:radial-gradient(circle at 50% 45%,#f0c9a4,#d49a6a 70%,#b97a46)}
.hero-badge{position:absolute;left:345px;top:24px;width:186px;height:186px;border-radius:50%;background:var(--white);
  border:2px solid #b783c8;text-align:center;font-family:"Didact Gothic",sans-serif}
.hero-badge .l1{color:var(--purple);font-size:25px;margin-top:27px}
.hero-badge .l2{color:#222;font-size:25px;margin-top:-2px}
.hero-badge .l3{color:var(--violet);font-size:14px;margin-top:0}
.hero-badge .l4{color:#222;font-size:14px;line-height:15px;margin-top:22px}
.dots{position:absolute;left:352px;top:218px;display:flex;gap:8px}
.dots span{width:12px;height:12px;border-radius:50%;background:#e9e9e9;border:1.5px solid #999}
.dots span.on{background:var(--pink);border-color:#eee}

.call-band{position:absolute;left:0;top:323px;width:779px;height:81px;background:var(--dark)}
.call-photo{position:absolute;left:52px;top:2px;width:86px;height:79px;border-radius:42px 42px 6px 6px;background:radial-gradient(circle at 50% 40%,#e9b48f,#c2552f 60%,#8a2f1c)}
.call-label{position:absolute;left:143px;top:22px;font-family:"Didact Gothic",sans-serif;font-size:28px;color:var(--magenta)}
.call-number{position:absolute;left:199px;top:20px;font-family:"Didact Gothic",sans-serif;font-size:30px;color:var(--white);text-decoration:none;letter-spacing:1px}
.call-note{position:absolute;left:422px;top:24px;font-family:"Didact Gothic",sans-serif;font-size:15px;line-height:15px;color:var(--magenta)}

.intro-title{position:absolute;left:57px;top:412px;font-family:"Didact Gothic",sans-serif;font-size:18px;color:var(--purple)}
.flourish{position:absolute;width:86px;height:14px;border-radius:7px}
.intro-text{position:absolute;left:59px;top:462px;width:445px;font-size:9px;line-height:14.8px;color:#555}
.intro-text p+p{margin-top:15px}

.special{position:absolute;left:525px;top:414px;width:203px;height:209px;background:var(--pink);color:#222;text-align:center;
  font-family:"Didact Gothic",sans-serif}
.special-inner{position:absolute;left:8px;top:8px;right:8px;bottom:8px;border:1px dashed rgba(255,255,255,.5)}
.special h3{font-weight:400;color:var(--white);font-size:17px;line-height:20px;margin-top:10px}
.special .sub{font-size:14px;line-height:15px;margin-top:26px;padding-bottom:5px;margin-left:10px;margin-right:10px;border-bottom:1px solid rgba(255,255,255,.5)}
.special .body{color:var(--white);font-size:13.5px;line-height:15px;margin-top:8px;padding:0 6px}
.btn{position:absolute;display:block;background:var(--darker);color:var(--white);border-radius:14px;border:1px dashed #888;
  font-family:"Didact Gothic",sans-serif;text-align:center;text-decoration:none}
.special .btn{left:50px;top:196px;width:107px;height:27px;line-height:25px;font-size:15px}

.services{position:absolute;left:0;top:654px;width:779px;height:344px;
  background:linear-gradient(180deg,#c93a88,#b2409b 45%,#9a3ab0 75%,#b548a2)}
.services h2{position:absolute;left:0;width:779px;top:14px;text-align:center;font-weight:400;color:var(--white);font-size:18px;font-family:"Didact Gothic",sans-serif}
.svc{position:absolute;top:68px;width:225px;text-align:center;color:var(--white)}
.svc .pic{width:138px;height:138px;border-radius:50%;margin:0 auto;border:3px solid #5a2a5e}
.svc h3{font-weight:400;font-family:"Didact Gothic",sans-serif;font-size:16px;margin-top:6px}
.svc p{font-size:9px;line-height:14.8px;margin-top:3px;letter-spacing:.2px}
.svc .btn{left:52px;top:274px;width:108px;height:27px;line-height:25px;font-size:14px}

.footer{position:absolute;left:0;top:998px;width:779px;height:176px;background:var(--dark)}
.footer h4{position:absolute;top:5px;font-weight:400;font-family:"Didact Gothic",sans-serif;font-size:15px;color:var(--magenta);
  padding-bottom:4px;border-bottom:1px solid #ccc}
.posts{position:absolute;left:57px;top:34px;width:202px;list-style:none}
.posts li{font-size:9px;color:var(--white);height:20.3px;line-height:18px;border-bottom:1px dashed #666}
.contact{position:absolute;left:274px;top:32px;width:220px;color:var(--white);font-size:9px;line-height:14.8px}
.contact .row{position:relative;padding-left:17px}
.contact svg{position:absolute;left:0;top:2px}
.social{position:absolute;top:127px;width:34px;height:34px;border-radius:50%;background:var(--pink);border:2px solid var(--white)}
.footer-photo{position:absolute;left:515px;top:985px;width:235px;height:215px;border-radius:110px 110px 0 0;
  background:radial-gradient(circle at 45% 35%,#f1d9cc,#cfa690 55%,#3b3436 80%)}
.copyright{position:absolute;left:0;top:1174px;width:779px;height:26px;background:var(--bar);color:var(--white);font-size:7.5px;line-height:26px;text-align:center}
.copyright a{color:var(--white);font-weight:600}
</style>
</head>
<body>

<header class="site-header">
  <div class="brand">Maple Cove Laser Dermal Studio</div>
  <nav class="nav">
    <a class="active" href="#">Home</a><a href="#">About</a><a href="#">Skin Renewal</a><a href="#">Scar Removal</a><a href="#">Your Visit</a><a href="#">Conact</a><a href="#">Blog</a>
  </nav>
</header>

<section class="hero">
  <div class="hero-left" role="img" aria-label="Soft grey spa scene with a relaxing woman and white flowers"></div>
  <div class="hero-right" role="img" aria-label="Close-up portrait of a woman with glowing skin and orchids"></div>
  <div class="hero-photo" role="img" aria-label="Smiling woman portrait"></div>
  <div class="hero-badge">
    <div class="l1">Laser</div>
    <div class="l2">Skin Renewal</div>
    <div class="l3">is Innovative and Unique</div>
    <div class="l4">Restore your<br>youthful skin this<br>year!</div>
  </div>
  <div class="dots"><span class="on"></span><span></span><span></span><span></span></div>
</section>

<section class="call-band">
  <div class="call-photo" role="img" aria-label="Woman with curly red hair"></div>
  <span class="call-label">Call</span>
  <a class="call-number" href="tel:5554102736">555-410-2736</a>
  <div class="call-note">to schedule<br>your convenient appointment.</div>
</section>

<h1 class="intro-title" style="font-weight:400">Have you considered Laser Skin Renewal Therapy?</h1>
<div class="flourish" style="left:196px;top:439px;background:#3a2f3a;opacity:.85" role="img" aria-label="Decorative flourish"></div>
<div class="intro-text">
  <p>You will truly love laser skin renewal if your skin is showing signs of premature aging or the skin has sustained sun damage. Conditions such as excessive redness due to sun exposure or fine lines will be concerns of the past. In fact, laser skin therapy is a unique and innovative way to enjoy youthful and healthy skin without resorting to painful and inconvenient surgery. Both men and women are receiving benefits from laser skin therapy.</p>
  <p>The literature contains ample scientific evidence to support laser skin renewal. After this therapy, your skin will produce collagen, which reduces and minimizes the appearance of fine lines and wrinkles. Imagine getting all this with minimal pain and no downtime? Doesn't it make you feel like getting in touch with our laser skin specialist today?</p>
</div>

<aside class="special">
  <div class="special-inner"></div>
  <h3>New Years<br>Resolution Special!</h3>
  <div class="flourish" style="left:58px;top:54px;width:86px;height:12px;background:#8e1f5a;opacity:.7" role="img" aria-label="Decorative flourish"></div>
  <div class="sub">Restore your youthful<br>skin this year!</div>
  <div class="body">Take advantage of our laser skin renewal specials for single or multiple sessions at low pricing.</div>
  <a class="btn" href="#">View All</a>
</aside>

<section class="services">
  <h2>Our Services</h2>
  <div class="flourish" style="left:337px;top:45px;width:105px;height:10px;background:#f1c7e3;opacity:.7" role="img" aria-label="Decorative flourish"></div>
  <div class="svc" style="left:47px">
    <div class="pic" style="background:radial-gradient(circle at 50% 45%,#f6dccb,#e0b294 70%)" role="img" aria-label="Smiling woman touching her face"></div>
    <h3>Skin Renewal</h3>
    <p>Laser skin renewal treatment could be just what you need to maintain your youthful appearance and get soft, smooth and evenly toned skin.</p>
    <a class="btn" href="#">Read More</a>
  </div>
  <div class="svc" style="left:280px">
    <div class="pic" style="border-color:#7a3ea0;background:radial-gradient(circle at 50% 50%,#d99a8c,#e4b2a2 70%)" role="img" aria-label="Close-up of a skin scar"></div>
    <h3>Scar Removal</h3>
    <p>Laser scar removal is affordable, safe and effective. Are your scars causing you to hide in embarrassment? Do they remind you…</p>
    <a class="btn" href="#" style="left:59px">Read More</a>
  </div>
  <div class="svc" style="left:512px">
    <div class="pic" style="border-color:#7a3ea0;background:radial-gradient(circle at 50% 50%,#f2d6c4,#e8c0a8 70%,#f5f0ee)" role="img" aria-label="Hands holding a foot with a plantar wart"></div>
    <h3>Wart Removal</h3>
    <p>Get Rid Of Stubborn Plantar Warts With Laser Wart Removal Technique Before you know more about laser wart removal technique,</p>
    <a class="btn" href="#" style="left:55px">Read More</a>
  </div>
</section>

<footer class="footer">
  <h4 style="left:57px;width:203px">Recent Post</h4>
  <ul class="posts">
    <li>The Benefits of Laser Skin Rejuvenation</li>
    <li>The Benefits of Laser Skin Rejuvenation</li>
    <li>The Benefits of Laser Skin Rejuvenation</li>
    <li>The Benefits of Laser Skin Rejuvenation</li>
    <li>The Benefits of Laser Skin Rejuvenation</li>
    <li>The Benefits of Laser Skin Rejuvenation</li>
  </ul>
  <h4 style="left:274px;width:203px">Contact With Us</h4>
  <div class="contact">
    <div class="row"><svg width="10" height="13" viewBox="0 0 10 13"><path d="M5 0a5 5 0 0 0-5 5c0 3.5 5 8 5 8s5-4.5 5-8a5 5 0 0 0-5-5zm0 7a2 2 0 1 1 0-4 2 2 0 0 1 0 4z" fill="#fff"/></svg>Maple Cove Laser Dermal Studio<br>Harborview Medical Plaza<br>2040 Lakeshore Dr, Suite 12<br>Maple Cove, TX 75510</div>
    <div class="row"><svg width="12" height="12" viewBox="0 0 24 24"><path d="M6.6 10.8a15.1 15.1 0 0 0 6.6 6.6l2.2-2.2a1 1 0 0 1 1-.25 11.4 11.4 0 0 0 3.6.57 1 1 0 0 1 1 1V20a1 1 0 0 1-1 1A17 17 0 0 1 3 4a1 1 0 0 1 1-1h3.5a1 1 0 0 1 1 1c0 1.25.2 2.45.57 3.6a1 1 0 0 1-.25 1z" fill="#fff"/></svg><a href="tel:5554102736" style="color:#fff;text-decoration:none">(555) 410-2736</a></div>
    <div class="row"><svg width="13" height="10" viewBox="0 0 13 10"><rect width="13" height="10" rx="1" fill="#fff"/><path d="M0.5 1l6 4.5 6-4.5" stroke="#2f2a30" fill="none"/></svg>info@maplecovelaserdermalstudio.com</div>
  </div>
  <a class="social" style="left:308px" href="#" aria-label="Social profile one"></a>
  <a class="social" style="left:355px" href="#" aria-label="Social profile two"></a>
  <a class="social" style="left:403px" href="#" aria-label="Social profile three"></a>
</footer>
<div class="footer-photo" role="img" aria-label="Woman with dark hair and clear skin holding a white feather"></div>

<div class="copyright">© <a href="http://maplecovelaserdermalstudio.com">Maple Cove Laser Dermal Studio</a> - 2014. All Rights Reserved.</div>

</body>
</html>
```